Etiketten für Schaps
Zielgruppe
Erzeugung hochwertiger Spirituosen wie Vodka, Gin, Liköre, Schnäpse. Das Produktporfolio reicht vom klassischem Vodka bis zu Absinth oder Kräuterbitter. Finden Sie unsere Produkte unter: www.brunecker-destille.at
Zielgruppe: Export nach Asien bzw. Afrika an die immer größer werdende Bevölkerungsschicht, die europäische Qualität schätzt. Fokus auf das österr. Image: K. u. K Zeit, Bergfalke, Sissy, Tradition, Kultur
Gesucht wird ein klassisches Spirituosenetikett
Aufgabenstellung
Gestaltung eines Vorderetiketts für eine eckige Flasche mit schwarzer Kapsel mit goldenem Aufdruck.
Verwendung des Logos 'B - Bergfalke ' (siehe Anlage), es soll jedoch neben Vodka und Gin auch eine Schnapsserie entwickelt werden: Sorten: Himbeergeist, Marillenschnaps, Williams-Christ-Birnenschnaos, Obstschnaps, Haselnuss-Schnaps
Größe des Etiketts: konisch, Breite oben: 53mm, Breite unten: 40 mll, Länge: max 150 mm, Ränder gewölbt, siehe
Stanze (siehe Anlage).
Die Farbe sollte in den Farben Gold/Schwarz gehalten werden, ev. auch eine rot-weiß-rote Fahne o.ä. als Hinweis auf die Herkunft
Ev. auch mit Fruchtabbildungen, diese können auch aus kommerziellen Bilddatenbanken genommen werden.

```html
<!DOCTYPE html>
<html lang="de">
<head>
<meta charset="utf-8">
<title>Bergfalke Himbeergeist – Etiketten</title>
<link rel="stylesheet" href="https://fonts.googleapis.com/css2?family=Lato:wght@400;700&family=Playfair+Display:wght@900&family=Great+Vibes&display=swap">
<style>
  :root {
    --paper: #ffffff;
    --label-ground: #f3f3f3;
    --band: #1d1d1d;
    --black: #000000;
    --gold: #c9a95a;
    --gold-dark: #8f6f2c;
    --gold-light: #f1dc9c;
    --keyline: #a8a8a8;
    --flag-red: #b0343c;
    --berry: #c8334c;
    --leaf: #8cbf3a;
  }
  * { box-sizing: border-box; margin: 0; padding: 0; }
  html, body { width: 1200px; height: 3158px; overflow: hidden; background: var(--paper); }
  .sheet { position: relative; width: 1200px; height: 3158px; }

  /* front label – all parts positioned against the label itself */
  .front-label {
    position: absolute; left: 121px; top: 199px; width: 940px; height: 1567px;
    background: var(--label-ground); border: 2px solid var(--keyline);
  }
  .front-band {
    position: absolute; left: 281px; top: -2px; width: 375px; height: 1573px;
    background: var(--band);
  }
  .emblem { position: absolute; display: block; }
  .emblem-name {
    font-family: "Lato", sans-serif; font-weight: 400; fill: var(--gold);
    letter-spacing: 2px;
  }
  .front-emblem { left: 212px; top: 107px; width: 512px; height: 646px; }

  .fruit-art {
    position: absolute; left: 331px; top: 788px; width: 218px; height: 162px;
    background: radial-gradient(circle at 62% 60%, var(--berry) 0 22%, transparent 23%),
                radial-gradient(ellipse at 40% 45%, var(--leaf) 0 45%, transparent 46%);
    border-radius: 40%;
  }

  .variety-banner {
    position: absolute; left: 258px; top: 957px; width: 420px; height: 170px;
    background: var(--black); border: 5px solid var(--gold);
    transform: rotate(-8deg);
    display: flex; flex-direction: column; align-items: center; justify-content: center;
    font-family: "Playfair Display", serif; font-weight: 900; color: var(--gold);
    font-size: 64px; line-height: 0.98; letter-spacing: 2px; text-align: center;
  }

  .quality-mark {
    position: absolute; left: 348px; top: 1168px; width: 240px;
    font-family: "Great Vibes", cursive; font-size: 60px; line-height: 1; color: var(--gold);
    text-align: center; transform: rotate(-8deg);
  }

  .portrait {
    position: absolute; left: 378px; top: 1252px; width: 180px; height: 180px;
    border-radius: 50%; border: 4px solid var(--gold);
    background: radial-gradient(circle at 50% 45%, #c9a48c, #7b6a5a 60%, #3d4a6a);
  }

  .origin-flag {
    position: absolute; left: 391px; top: 1470px; width: 152px; height: 40px;
    background: var(--paper); padding: 5px 6px;
    display: flex; flex-direction: column; justify-content: space-between;
  }
  .origin-flag span { display: block; height: 9px; background: var(--flag-red); }

  /* round capsule label */
  .cap-label {
    position: absolute; left: 95px; top: 1905px; width: 330px; height: 330px;
    border-radius: 50%; border: 2px solid var(--keyline); background: var(--paper);
  }
  .cap-emblem { left: 65px; top: 40px; width: 198px; height: 250px; }

  /* neck strips */
  .neck-sheet {
    position: absolute; left: 91px; top: 2266px; width: 1044px; height: 627px;
    border: 2px solid var(--keyline); background: var(--paper);
  }
  .neck-strip { position: absolute; top: -2px; width: 254px; height: 629px; background: var(--band); }
  .neck-strip:nth-child(1) { left: 52px; }
  .neck-strip:nth-child(2) { left: 395px; }
  .neck-strip:nth-child(3) { left: 738px; }
  .neck-emblem { left: -34px; top: 190px; width: 322px; height: 407px; }
</style>
</head>
<body>
<main class="sheet">

  <svg width="0" height="0" style="position:absolute" aria-hidden="true">
    <defs>
      <linearGradient id="goldRing" x1="0" y1="0" x2="1" y2="1">
        <stop offset="0" stop-color="#8f6f2c"/>
        <stop offset="0.45" stop-color="#f1dc9c"/>
        <stop offset="1" stop-color="#8f6f2c"/>
      </linearGradient>
      <symbol id="brandEmblem" viewBox="0 0 524 662">
        <ellipse cx="262" cy="331" rx="262" ry="331" fill="#000"/>
        <ellipse cx="262" cy="331" rx="238" ry="304" fill="none" stroke="url(#goldRing)" stroke-width="9"/>
        <ellipse cx="262" cy="331" rx="222" ry="288" fill="none" stroke="url(#goldRing)" stroke-width="20" stroke-dasharray="4 7"/>
        <ellipse cx="262" cy="331" rx="206" ry="272" fill="none" stroke="url(#goldRing)" stroke-width="4"/>
      </symbol>
    </defs>
  </svg>

  <section class="front-label" aria-label="Vorderetikett">
    <div class="front-band"></div>

    <svg class="emblem front-emblem" viewBox="0 0 524 662">
      <use href="#brandEmblem"/>
      <text class="emblem-name" x="262" y="352" text-anchor="middle" font-size="66">BERGFALKE</text>
    </svg>

    <div class="fruit-art" role="img" aria-label="Himbeeren mit grünen Blättern"></div>

    <div class="variety-banner"><span>HIMBEER</span><span>GEIST</span></div>

    <div class="quality-mark">Premium</div>

    <div class="portrait" role="img" aria-label="Historisches Porträt eines Kaisers in Uniform"></div>

    <div class="origin-flag" role="img" aria-label="Rot-weiß-rote Fahne"><span></span><span></span></div>
  </section>

  <section class="cap-label" aria-label="Kapseletikett">
    <svg class="emblem cap-emblem" viewBox="0 0 524 662">
      <use href="#brandEmblem"/>
      <text class="emblem-name" x="262" y="352" text-anchor="middle" font-size="66">BERGFALKE</text>
    </svg>
  </section>

  <section class="neck-sheet" aria-label="Halsetiketten">
    <div class="neck-strip">
      <svg class="emblem neck-emblem" viewBox="0 0 524 662">
        <use href="#brandEmblem"/>
        <text class="emblem-name" x="262" y="352" text-anchor="middle" font-size="66">BERGFALKE</text>
      </svg>
    </div>
    <div class="neck-strip">
      <svg class="emblem neck-emblem" viewBox="0 0 524 662">
        <use href="#brandEmblem"/>
        <text class="emblem-name" x="262" y="352" text-anchor="middle" font-size="66">BERGFALKE</text>
      </svg>
    </div>
    <div class="neck-strip">
      <svg class="emblem neck-emblem" viewBox="0 0 524 662">
        <use href="#brandEmblem"/>
        <text class="emblem-name" x="262" y="352" text-anchor="middle" font-size="66">BERGFALKE</text>
      </svg>
    </div>
  </section>

</main>
</body>
</html>
```